Harbor Pine builders of ny Roofing flyer

We would like to create a flyer for roofing customers : commercial / real estate management / business / schools /warehouses

Flat roof specialists
Waterproofing experts

Special flat roof re layer @ 3.00 per sq ft

Roof leak repairs
Flashing
Waterproofing

Call 555 3019462

For pictures find torch down roof applications
Flat roofs ny

```html
<!DOCTYPE html>
<html lang="en">
<head>
<meta charset="utf-8">
<title>Harbor Pine builders of ny – Flat Roof Flyer</title>
<link rel="stylesheet" href="https://fonts.googleapis.com/css2?family=Anton&display=swap">
<style>
  :root {
    --brand-green: #133a22;
    --accent-red: #e0382d;
    --soft-gray: #c6c7c9;
    --paper: #ffffff;
    --backdrop: #e6e6e6;
    --photo-sky: #c9d3c4;
    --photo-roof: #a7a8a3;
  }
  html, body {
    margin: 0;
    padding: 0;
    width: 1200px;
    height: 971px;
    overflow: hidden;
    background: var(--backdrop);
  }
  .flyer {
    position: absolute;
    left: 240px;
    top: 21px;
    width: 719px;
    height: 929px;
    box-shadow: 0 6px 18px rgba(0,0,0,0.25);
    font-family: 'Anton', 'Oswald', sans-serif;
  }
  .flyer svg { display: block; width: 100%; height: 100%; }
  .brand-name { fill: var(--brand-green); }
  .headline-green { fill: var(--brand-green); }
  .headline-red { fill: var(--accent-red); }
  .service-item { fill: var(--brand-green); font-size: 60px; }
  .offer-text { fill: var(--paper); }
  .cta-text { fill: var(--paper); font-size: 62px; }
  .tick { fill: none; stroke: var(--brand-green); stroke-width: 7; stroke-linecap: round; stroke-linejoin: round; }
</style>
</head>
<body>
<div class="flyer">
  <svg viewBox="0 0 910 1176" xmlns="http://www.w3.org/2000/svg">
    <defs>
      <linearGradient id="roofPhotoTone" x1="0" y1="0" x2="0" y2="1">
        <stop offset="0" stop-color="#dfe3dc"/>
        <stop offset="0.15" stop-color="var(--photo-sky)"/>
        <stop offset="0.22" stop-color="#6f7a73"/>
        <stop offset="0.45" stop-color="#8f918d"/>
        <stop offset="1" stop-color="var(--photo-roof)"/>
      </linearGradient>
      <linearGradient id="headerFade" x1="0" y1="0" x2="0" y2="1">
        <stop offset="0" stop-color="#ffffff"/>
        <stop offset="1" stop-color="#eef0ee"/>
      </linearGradient>
    </defs>

    <!-- header -->
    <rect class="header" x="0" y="0" width="910" height="270" fill="url(#headerFade)"/>
    <g class="brand">
      <text class="brand-name" x="147" y="168" font-size="44" text-anchor="middle" textLength="200" lengthAdjust="spacingAndGlyphs">HARBOR PINE</text>
      <text class="brand-name" x="147" y="212" font-size="44" text-anchor="middle" textLength="200" lengthAdjust="spacingAndGlyphs">BUILDERS OF NY</text>
    </g>
    <text class="headline" x="278" y="143" font-size="66" textLength="525" lengthAdjust="spacingAndGlyphs"><tspan class="headline-green">FLAT ROOF </tspan><tspan class="headline-red">SPECIALISTS</tspan></text>
    <text class="headline" x="278" y="217" font-size="66" textLength="587" lengthAdjust="spacingAndGlyphs"><tspan class="headline-green">WATERPROOFING </tspan><tspan class="headline-red">EXPERTS</tspan></text>

    <!-- photo -->
    <rect class="hero-photo" x="0" y="270" width="910" height="531" fill="url(#roofPhotoTone)" role="img" aria-label="Roofer in a yellow hard hat kneeling on a flat roof, rolling out torch-down roofing membrane"/>

    <!-- lower panel -->
    <rect class="services-panel" x="0" y="801" width="910" height="272" fill="var(--paper)"/>
    <polygon class="offer-gray" points="387,1073 662,995 910,1055 910,1073" fill="var(--soft-gray)"/>
    <polygon class="offer-red" points="472,736 910,736 910,1055 662,995" fill="var(--accent-red)"/>

    <g class="services">
      <path class="tick" d="M60 862 L74 880 L102 842"/>
      <text class="service-item" x="120" y="893">Roof leak repairs</text>
      <path class="tick" d="M60 931 L74 949 L102 911"/>
      <text class="service-item" x="120" y="962">Flashing</text>
      <path class="tick" d="M60 999 L74 1017 L102 979"/>
      <text class="service-item" x="120" y="1030">Waterproofing</text>
    </g>

    <g class="offer" text-anchor="end">
      <text class="offer-text" x="862" y="810" font-size="46">Special flat</text>
      <text class="offer-text" x="862" y="858" font-size="46">roof re layer</text>
      <text class="offer-text" x="862" y="950" font-size="86">@ 3.00</text>
      <text class="offer-text" x="862" y="985" font-size="30">per sq ft</text>
    </g>

    <!-- call to action -->
    <rect class="cta-band" x="0" y="1073" width="910" height="103" fill="var(--brand-green)"/>
    <text class="cta-text" x="455" y="1150" text-anchor="middle">Call 555 3019462</text>
  </svg>
</div>
</body>
</html>
```